Post card selling a software for elderly visitor security

I need a postcard re-design that will entice children of elderly parents to sign-up to monitor the visitors (via online reporting dashboard) that care for them. These elderly residents live in a nursing home and many can't remember who came in the room to care for them. This is a major safety and security issue and adult children sometimes have no way of knowing who is visiting their parents. Our software provides an online reporting dashboard and sends text messages to adult children when a visitor arrives at the nursing home.

Target Market(s)

women between 50-65

Industry/Entity Type

Nursing Home

Colors

Designer to choose colors to be used in the design.

Requirements
Must have
• Must have Two questions: Are you the Primary Guardian of a resident in this community? If so, would you like to know who is visiting them?
• Must have a desktop computer and phone
• Needs to have a white background

```html
<!DOCTYPE html>
<html lang="en">
<head>
<meta charset="utf-8">
<title>Resident Visitor Alerts Postcard</title>
<link href="https://fonts.googleapis.com/css2?family=Poppins:wght@600;700&family=Roboto:ital,wght@0,400;0,500;0,700;1,400;1,700&family=Roboto+Slab:wght@400;700&display=swap" rel="stylesheet">
<style>
:root{
  --headline-blue:#1479b8;
  --headline-green:#5aab3e;
  --ink:#1b1b1b;
  --device-black:#111214;
  --screen-blue-top:#b9cbe8;
  --screen-blue-bottom:#5a74c4;
  --sidebar:#3b4a6e;
  --tile-green:#3fae49;
  --tile-purple:#7a5aa8;
  --tile-orange:#f08a4b;
  --tile-red:#ee5253;
  --tile-blue:#3b88c9;
  --button-blue:#3aa0d8;
  --alert-red:#e8262b;
  --call-blue:#4a5bb0;
  --resident-red:#e02424;
}
*{margin:0;padding:0;box-sizing:border-box}
html,body{width:1200px;height:850px;overflow:hidden;background:#fff}
.card{position:relative;width:1200px;height:850px;background:#fff;font-family:"Roboto",Arial,sans-serif;color:var(--ink)}
.headline{position:absolute;left:0;right:0;top:38px;text-align:center;font-family:"Poppins",Arial,sans-serif;font-weight:700;font-size:58px;line-height:60px;letter-spacing:-1.5px;color:var(--headline-blue)}
.headline .accent{color:var(--headline-green)}
.divider{position:absolute;left:180px;width:840px;top:180px;height:6px;background:radial-gradient(ellipse at center,rgba(0,0,0,.12),rgba(0,0,0,0) 70%)}
.subhead{position:absolute;left:0;right:0;top:200px;text-align:center;font-family:"Poppins",Arial,sans-serif;font-weight:600;font-size:41px;letter-spacing:-.8px;color:var(--ink)}
.monitor-frame{position:absolute;left:241px;top:287px;width:646px;height:382px;background:var(--device-black);border-radius:14px 14px 0 0}
.monitor-chin{position:absolute;left:241px;top:669px;width:646px;height:58px;background:linear-gradient(#e4e5e7,#c9cacd);border-radius:0 0 10px 10px}
.monitor-camera{position:absolute;left:562px;top:294px;width:4px;height:4px;border-radius:50%;background:#444}
.monitor-stand{position:absolute;left:460px;top:727px}
.screen{position:absolute;left:267px;top:311px;width:597px;height:334px;background:linear-gradient(var(--screen-blue-top),var(--screen-blue-bottom));overflow:hidden}
.browser{position:absolute;left:90px;top:7px;width:418px;height:330px;background:#fff;overflow:hidden}
.browser-tabs{height:10px;background:#dfe1e5;display:flex;gap:3px;padding:1px 4px 0 22px;font-size:4px;color:#555}
.browser-tabs span{background:#eceef1;padding:1px 6px;border-radius:2px 2px 0 0}
.browser-url{height:12px;background:#f4f5f7;border-bottom:1px solid #ddd;font-size:4.5px;color:#666;padding:3px 0 0 50px}
.sidebar{position:absolute;left:0;top:0;width:18px;height:100%;background:var(--sidebar)}
.sidebar i{position:absolute;left:4px;width:10px;height:8px;border-radius:2px}
.dash{position:absolute;left:18px;top:22px;right:0;bottom:0}
.dash-title{position:absolute;left:5px;top:6px;font-weight:700;font-size:17px}
.download-btn{position:absolute;left:259px;top:7px;width:134px;height:17px;background:var(--button-blue);color:#fff;font-size:10px;font-weight:700;text-align:center;line-height:17px;border:1px solid #7cc3ea}
.date-range{position:absolute;left:5px;top:32px;font-size:10px;font-weight:700}
.resident-box{position:absolute;left:2px;top:48px;width:394px;height:25px;border:1px solid #d6d6d6;font-family:"Roboto Slab",Georgia,serif;font-size:15px;padding:2px 6px}
.tiles{position:absolute;left:2px;top:83px}
.tile{position:absolute;top:0;height:36px;color:#fff;font-size:10px;font-weight:500;padding:2px 3px}
.tile b{display:block;font-family:"Roboto Slab",Georgia,serif;font-size:12px}
.tile-family{left:0;width:89px;background:var(--tile-green)}
.tile-caregivers{left:93px;width:103px;background:var(--tile-purple)}
.tile-doctors{left:202px;width:54px;background:var(--tile-orange)}
.tile-alerts{left:261px;width:54px;background:var(--tile-red)}
.tile-signouts{left:321px;width:74px;background:var(--tile-blue)}
.history-label{position:absolute;left:2px;top:132px;font-size:10px;font-weight:500}
.history{position:absolute;left:2px;top:148px;width:370px;height:190px;font-size:8.5px}
.history div{position:absolute;white-space:nowrap}
.history .head{font-weight:700;top:0}
.c-date{left:0}.c-time{left:50px}.c-type{left:118px}.c-company{left:205px}.c-service{left:262px}.c-location{left:320px}
.avatar{position:absolute;left:374px;width:22px;height:22px;border-radius:50%;background:linear-gradient(#e8d2c0,#9fb6a8)}
.callout-lines{position:absolute;left:0;top:0}
.callout{position:absolute;left:572px;top:542px;width:225px;height:82px;background:#fff;border:1px solid #9a9a9a;border-radius:9px;padding:6px 8px;font-size:10px;line-height:13.5px;box-shadow:0 1px 3px rgba(0,0,0,.2)}
.callout-name{font-weight:700;font-size:12px;letter-spacing:.2px}
.callout-agency{font-style:italic}
.resident{color:var(--resident-red)}
.callout-photo{position:absolute;left:718px;top:542px;width:78px;height:78px;border-radius:50%;background:radial-gradient(circle at 50% 40%,#8a6a58,#3e8f85 70%,#c9b9a4);border:1px solid #bbb}
.phone{position:absolute;left:848px;top:432px;width:175px;height:368px;background:var(--device-black);border-radius:24px;box-shadow:0 6px 10px rgba(0,0,0,.25)}
.phone-speaker{position:absolute;left:63px;top:20px;width:48px;height:3px;border-radius:2px;background:#3a3a3a}
.phone-screen{position:absolute;left:5px;top:41px;width:164px;height:286px;background:linear-gradient(#b7c6e6,#7f95cc 70%,#6f86c0);overflow:hidden}
.alert-banner{height:37px;background:var(--alert-red);color:#fff;font-size:14.5px;text-align:center;line-height:40px;letter-spacing:.2px}
.alert-banner b{font-weight:700}
.alert-card{position:absolute;left:5px;top:64px;width:154px;height:151px;background:#fff;border-radius:8px;padding:32px 7px 0}
.alert-close{position:absolute;right:7px;top:4px;font-size:10px;font-weight:700}
.alert-title{text-align:center;font-weight:700;font-size:15px;border-bottom:1px solid #333;margin:0 4px 4px;padding-bottom:1px}
.alert-line{font-size:11px;line-height:16px;white-space:nowrap}
.alert-line b{font-weight:700}
.call-btn{display:block;margin:5px auto 0;width:58px;height:20px;background:var(--call-blue);color:#fff;font-size:11px;text-align:center;line-height:20px;border-radius:2px}
.alert-photo{position:absolute;left:57px;top:46px;width:48px;height:48px;border-radius:50%;background:radial-gradient(circle at 50% 40%,#8a6a58,#3e8f85 70%,#d9cdbb)}
.dock{position:absolute;left:14px;top:260px;display:flex;gap:8px}
.dock i{width:30px;height:22px;border-radius:6px;background:rgba(255,255,255,.28)}
.home-button{position:absolute;left:75px;top:333px;width:26px;height:26px;border-radius:50%;background:#2a2b2e;border:1px solid #555}
</style>
</head>
<body>
<div class="card">
  <h1 class="headline">ARE YOU THE <span class="accent">PRIMARY GUARDIAN</span> OF<br>A RESIDENT IN THIS COMMUNITY?</h1>
  <div class="divider"></div>
  <p class="subhead">If so, would you like to know who is visiting them?</p>

  <div class="monitor">
    <div class="monitor-frame"></div>
    <div class="monitor-camera"></div>
    <div class="monitor-chin"></div>
    <svg class="monitor-stand" width="210" height="82" viewBox="0 0 210 82">
      <defs><linearGradient id="standShade" x1="0" x2="1"><stop offset="0" stop-color="#bfc0c3"/><stop offset=".5" stop-color="#eceded"/><stop offset="1" stop-color="#b5b6b9"/></linearGradient></defs>
      <path d="M45 0 H165 L178 70 H32 Z" fill="url(#standShade)"/>
      <rect x="10" y="70" width="190" height="8" rx="3" fill="#d8d9db"/>
    </svg>
    <div class="screen">
      <div class="browser">
        <div class="sidebar">
          <i style="top:56px;background:#f0b23a"></i>
          <i style="top:90px;background:#e8563a"></i>
          <i style="top:128px;background:#e0703a"></i>
          <i style="top:160px;background:#5aa0e0"></i>
        </div>
        <div class="browser-tabs"><span>Inbox</span><span>Home</span><span>Visitor</span><span>Report</span><span>Dashboard</span></div>
        <div class="browser-url">https://visitlog.example.com/communities/report</div>
        <div class="dash">
          <div class="dash-title">Resident Visitor Report</div>
          <div class="download-btn">Download Visitor Report</div>
          <div class="date-range">showing visitor info from Aug, 21 - July2</div>
          <div class="resident-box">Ruth Palmer - Assisted Living</div>
          <div class="tiles">
            <div class="tile tile-family">Family Visitors<b>13</b></div>
            <div class="tile tile-caregivers">Private Caregivers<b>12</b></div>
            <div class="tile tile-doctors">Doctors<b>7</b></div>
            <div class="tile tile-alerts">Alerts<b>3</b></div>
            <div class="tile tile-signouts">Sign-outs<b>12</b></div>
          </div>
          <div class="history-label">VISIT HISTORY</div>
          <div class="history">
            <div class="head c-date">Date</div>
            <div class="head c-time">Time In</div>
            <div class="head c-type">Visit Type</div>
            <div class="head c-company">Company</div>
            <div class="head c-service">Service</div>
            <div class="head c-location">Location</div>

            <div class="c-date" style="top:16px">1/3/19</div>
            <div class="c-time" style="top:16px">11:03 AM</div>
            <div class="c-type" style="top:16px">Dr. Alan Reyes</div>
            <div class="c-company" style="top:16px">CarePoint</div>
            <div class="c-service" style="top:16px">Check-up</div>
            <div class="c-location" style="top:16px">Doc office</div>

            <div class="c-date" style="top:40px">1/4/19</div>
            <div class="c-time" style="top:40px">7:03 AM</div>
            <div class="c-type" style="top:40px">Nora Whitfield</div>
            <div class="c-company" style="top:40px">Elm Home</div>
            <div class="c-service" style="top:40px">Home Health</div>
            <div class="c-location" style="top:40px">Community</div>

            <div class="c-date" style="top:88px">1/4/19</div>
            <div class="c-time" style="top:88px">4:03 PM</div>
            <div class="c-type" style="top:88px">Kate Dunmore</div>

            <div class="c-date" style="top:121px">1/5/19</div>
            <div class="c-time" style="top:121px">11:03 AM</div>
            <div class="c-type" style="top:121px">Lucy Hartman</div>

            <div class="c-date" style="top:157px">1/6/19</div>
            <div class="c-time" style="top:157px">12:01 AM</div>
            <div class="c-type" style="top:157px">Mary Olsen</div>
            <div class="c-company" style="top:157px">Family</div>
            <div class="c-service" style="top:157px">Visit</div>
            <div class="c-location" style="top:157px">Community</div>
          </div>
          <div class="avatar" role="img" aria-label="Portrait photo of the visiting doctor" style="top:160px"></div>
          <div class="avatar" role="img" aria-label="Portrait photo of the home health aide" style="top:186px"></div>
          <div class="avatar" role="img" aria-label="Portrait photo of a family visitor" style="top:298px"></div>
        </div>
      </div>
    </div>
    <svg class="callout-lines" width="1200" height="850" viewBox="0 0 1200 850">
      <line x1="477" y1="542" x2="584" y2="624" stroke="#111" stroke-width="1.5"/>
      <line x1="477" y1="542" x2="574" y2="542" stroke="#111" stroke-width="1.5"/>
    </svg>
    <div class="callout">
      <div class="callout-name">NORA WHITFIELD, PA</div>
      <div class="callout-agency">Home Health Agency</div>
      <div class="resident">Resident: Edith Carlow</div>
      <div>Check-in time: 3:15 PM</div>
      <div>Check-out time: 3:35 PM</div>
    </div>
    <div class="callout-photo" role="img" aria-label="Photo of the home health aide in teal scrubs holding a tablet"></div>
  </div>

  <div class="phone">
    <div class="phone-speaker"></div>
    <div class="phone-screen">
      <div class="alert-banner">VISITOR <b>TEXT</b> ALERT</div>
      <div class="alert-card">
        <span class="alert-close">x</span>
        <div class="alert-title">VISITOR</div>
        <div class="alert-line"><b>Name:</b> Nora Whitfield</div>
        <div class="alert-line"><b>Agency:</b> Elm Home Health</div>
        <div class="alert-line resident"><b><i>Resident:</i></b> <i>Edith Carlow</i></div>
        <div class="alert-line"><b>Sign-in:</b> 3:15 pm EST</div>
        <span class="call-btn">CALL</span>
      </div>
      <div class="alert-photo" role="img" aria-label="Photo of the home health aide in teal scrubs"></div>
      <div class="dock"><i></i><i></i><i></i><i></i></div>
    </div>
    <div class="home-button"></div>
  </div>
</div>
</body>
</html>
```